Business card design for Summit Wallcrafters required

Our company "Boardwork Ontrack Polishing Venture" needs business cards. Make the business cards be found easily amongst 100 other construction business cards. White background, logo centered and large.

Target Market(s)

Customers or builders who need a drywaller and customers who need a very high quality drywaller.

Industry/Entity Type

Construction

Contact Information for Business Card

The business logo centered and large with "Serving Ridgefall County 15+years" in black Italic, and 2 telephone numbers centered beneath written: Kim / Dale: 403-555-0182, and 403-555-0347 beneath. The business cards will be printed in metal with rounded corners.

Colors
ec1f27

Requirements
Must have
• The selected logo. Must be able to see "BOARDWORK" from a distance. Must stick out from other business cards.

```html
<!DOCTYPE html>
<html lang="en">
<head>
<meta charset="utf-8">
<title>Boardwork Ontrack Polishing Venture – Business Card</title>
<link rel="stylesheet" href="https://fonts.googleapis.com/css2?family=Exo+2:ital,wght@0,500;0,700;1,500;1,600&display=swap">
<style>
  :root {
    --brand-red: #ec1f27;
    --ink: #222222;
    --ink-soft: #333333;
    --card-white: #ffffff;
    --rule-black: #1a1a1a;
  }
  * { margin: 0; padding: 0; box-sizing: border-box; }
  html, body {
    width: 1200px;
    height: 686px;
    overflow: hidden;
    background: var(--card-white);
  }
  .card {
    position: relative;
    width: 1200px;
    height: 686px;
    background: var(--card-white);
    font-family: "Exo 2", sans-serif;
    overflow: hidden;
  }
  .side-band {
    position: absolute;
    left: 0; top: 0;
    width: 153px;
    height: 686px;
    background: var(--brand-red);
    border-radius: 46px 0 0 46px;
  }
  .side-rule {
    position: absolute;
    left: 158px; top: 0;
    width: 3px;
    height: 686px;
    background: var(--rule-black);
  }
  .mount-hole {
    position: absolute;
    left: 104px; top: 618px;
    width: 28px; height: 28px;
    border-radius: 50%;
    background: var(--card-white);
  }
  .brand-square {
    position: absolute;
    left: 57px; top: 97px;
    width: 166px; height: 177px;
    background: var(--brand-red);
    border: 14px solid var(--card-white);
  }
  .brand-name {
    position: absolute;
    left: 257px; top: 124px;
    font-size: 74px;
    font-weight: 700;
    line-height: 1;
    color: var(--brand-red);
    letter-spacing: 1px;
    white-space: nowrap;
  }
  .brand-tagline {
    position: absolute;
    left: 262px; top: 225px;
    width: 672px;
    font-size: 25px;
    font-weight: 500;
    letter-spacing: 14.5px;
    color: var(--ink-soft);
    white-space: nowrap;
  }
  .service-line {
    position: absolute;
    left: 270px; top: 363px;
    font-size: 39px;
    font-style: italic;
    font-weight: 600;
    color: var(--ink);
    white-space: nowrap;
  }
  .contacts {
    position: absolute;
    left: 270px; top: 505px;
    font-size: 34px;
    font-style: italic;
    font-weight: 500;
    line-height: 44px;
    list-style: none;
  }
  .contact-name { color: var(--brand-red); }
  .contact-number { color: var(--ink); }
</style>
</head>
<body>
  <div class="card">
    <div class="side-band"></div>
    <div class="side-rule"></div>
    <div class="mount-hole"></div>

    <div class="brand-square"></div>
    <div class="brand-name">Boardwork Ontrack</div>
    <div class="brand-tagline">POLISHING VENTURE</div>

    <p class="service-line">Serving Ridgefall County 15+years</p>

    <ul class="contacts">
      <li><span class="contact-name">&nbsp;Kim : </span><span class="contact-number">403-555-0182</span></li>
      <li><span class="contact-name">Dale : </span><span class="contact-number">403-555-0347</span></li>
    </ul>
  </div>
</body>
</html>
```